International Clinical Software Company needs a new business card design

We are looking for a new business card design for our company that has recently expanded into the UK market, making us a multinational company.
After having rebranded our website and produced a new style guide, we are looking for a business card that is creative and attention grabbing, while being consistent with the style and colour scheme used on the new website, www.brookvale.example
We produce care management technology for the aged care market, but the main aspect we aim to communicate is the human element of our software, and the way it assists in providing better care for aged people, and stronger relationships between aged people and the staff that care for them.
Our current business card is a dark green with gold text, which makes the text quite difficult to read, not very aesthetically appealing and the colour scheme looks quite dated.
We would like something fresh and modern, that can still be colourful but doesn't use large blocks of dark colour, and uses the colours within our logo.
Something tying in with the leaves that are used in our logo could work quite nicely, along with the Autumn/Fall colours of soft greens, yellows and reds (also in our existing logo). However also happy to look at fresh, completely out of the box ideas we may not have yet considered.
Target Market(s)
The people that receive this business card work in the aged card or health industry and are either corporate/management level staff or clinical (Registered Nurses, care workers etc.)
Industry/Entity Type
Health Product
Contact Information for Business Card
Company Name - BrookvaleTech
Company locations: Harrowmere, Kestrel Bay, Ashdown Vale
Staff Details:
Staff name: Dermot Quill
Staff job title: Executive Chairman
Staff email: d.quill@brookvale.example
Office phone number: 01632 960418
Font styles to use
Other font styles liked:
- Calibri
Requirements
Must have
- Must include the BrookvaleTech brand name in it's current font
- Must include logo (3 leaves in gold circle)
- Must include Business Card Details
Nice to have
- Elements of gold
- White space
- Something autumn themed but not too cliched
Should not have
- No blue - used by a major competitor and we would like to differentiate from them
- Large blocks of dark green colour (the green that appears in our leaves on the logo on our current business card is the background colour and it is far too dark)

```html
<!DOCTYPE html>
<html lang="en">
<head>
<meta charset="utf-8">
<title>BrookvaleTech – Business Card</title>
<link href="https://fonts.googleapis.com/css2?family=Open+Sans:wght@300;400;600&display=swap" rel="stylesheet">
<style>
  :root {
    --page-bg: #e8e6e3;
    --card-white: #ffffff;
    --ink-grey: #4a4a4a;
    --ink-dark: #2b2b2b;
    --name-red: #b8283c;
    --brand-gold: #9c8460;
    --leaf-orange: #e0791f;
    --leaf-yellow: #f3d45a;
    --leaf-red: #c9412a;
    --leaf-mint: #cfe3b4;
    --icon-red: #c23a45;
  }
  * { box-sizing: border-box; margin: 0; padding: 0; }
  html, body {
    width: 1200px;
    height: 864px;
    overflow: hidden;
    background: var(--page-bg);
    font-family: "Open Sans", "Calibri", sans-serif;
  }
  .sheet {
    position: relative;
    width: 1200px;
    height: 864px;
  }
  .card {
    position: absolute;
    left: 280px;
    width: 640px;
    height: 366px;
    overflow: hidden;
    box-shadow: 0 2px 6px rgba(0,0,0,0.12);
  }

  /* Front */
  .card--front { top: 40px; }
  .front-artwork {
    position: absolute;
    inset: 0;
    background:
      radial-gradient(ellipse 45% 55% at 18% 30%, var(--leaf-orange) 0%, rgba(224,121,31,0) 70%),
      radial-gradient(ellipse 40% 40% at 35% 75%, var(--leaf-yellow) 0%, rgba(243,212,90,0) 70%),
      radial-gradient(ellipse 35% 45% at 70% 10%, var(--leaf-red) 0%, rgba(201,65,42,0) 65%),
      radial-gradient(ellipse 30% 40% at 95% 55%, var(--leaf-orange) 0%, rgba(224,121,31,0) 70%),
      linear-gradient(120deg, #e58a24 0%, #f2c04a 40%, var(--leaf-mint) 75%, #f0c25a 100%);
  }
  .front-wordmark {
    position: absolute;
    right: 80px;
    bottom: 44px;
    font-weight: 300;
    font-size: 54px;
    letter-spacing: 1px;
    color: var(--card-white);
  }

  /* Back */
  .card--back {
    top: 458px;
    background: var(--card-white);
  }
  .back-leaves {
    position: absolute;
    inset: 0;
    width: 640px;
    height: 366px;
  }
  .brand-lockup {
    position: absolute;
    top: 30px;
    right: 44px;
    display: flex;
    flex-direction: column;
    align-items: center;
  }
  .brand-lockup__dot {
    width: 48px;
    height: 48px;
    border-radius: 50%;
    background: var(--brand-gold);
    margin-bottom: 8px;
  }
  .brand-lockup__name {
    font-weight: 300;
    font-size: 28px;
    color: var(--brand-gold);
  }
  .person {
    position: absolute;
    left: 52px;
    top: 142px;
  }
  .person__name {
    font-weight: 600;
    font-size: 22px;
    color: var(--name-red);
    line-height: 1.1;
  }
  .person__title {
    font-weight: 400;
    font-size: 14px;
    color: var(--ink-grey);
  }
  .contact {
    position: absolute;
    right: 44px;
    bottom: 40px;
    list-style: none;
    text-align: right;
  }
  .contact__item {
    display: flex;
    justify-content: flex-end;
    align-items: center;
    gap: 10px;
    font-size: 15px;
    color: var(--ink-dark);
    line-height: 28px;
  }
  .contact__icon { width: 14px; height: 14px; flex: none; }
</style>
</head>
<body>
<main class="sheet">

  <section class="card card--front" aria-label="Business card front">
    <div class="front-artwork" role="img" aria-label="Photograph of soft-focus autumn maple leaves in orange, yellow and red"></div>
    <div class="front-wordmark">BrookvaleTech</div>
  </section>

  <section class="card card--back" aria-label="Business card back">
    <svg class="back-leaves" viewBox="0 0 640 366" role="img" aria-label="Illustration of a drift of autumn leaves in yellow, orange, red and green">
      <defs>
        <linearGradient id="leafDrift" x1="0" y1="0" x2="1" y2="1">
          <stop offset="0" stop-color="#f2d34f"/>
          <stop offset="0.35" stop-color="#e98a22"/>
          <stop offset="0.6" stop-color="#d8b43a"/>
          <stop offset="0.8" stop-color="#d5472e"/>
          <stop offset="1" stop-color="#e6a63a"/>
        </linearGradient>
      </defs>
      <path d="M110 0 H360 C380 40 400 70 450 110 C520 150 600 150 640 150 V250 C590 250 540 240 470 225 C400 215 350 230 320 210 C260 170 230 120 200 70 C180 40 140 20 110 0 Z"
            fill="url(#leafDrift)" opacity="0.9"/>
    </svg>

    <div class="brand-lockup">
      <span class="brand-lockup__dot"></span>
      <span class="brand-lockup__name">BrookvaleTech</span>
    </div>

    <div class="person">
      <p class="person__name">Dermot Quill</p>
      <p class="person__title">Executive Chairman</p>
    </div>

    <ul class="contact">
      <li class="contact__item">
        <span>d.quill@brookvale.example</span>
        <svg class="contact__icon" viewBox="0 0 14 14" aria-hidden="true">
          <rect x="0" y="2" width="14" height="10" fill="var(--icon-red)"/>
          <path d="M1 3 L7 8 L13 3" stroke="#fff" stroke-width="1.2" fill="none"/>
        </svg>
      </li>
      <li class="contact__item">
        <span>Harrowmere, Kestrel Bay, Ashdown Vale</span>
        <svg class="contact__icon" viewBox="0 0 14 14" aria-hidden="true">
          <path d="M7 0 C3.7 0 2 2.4 2 5 C2 8.5 7 14 7 14 C7 14 12 8.5 12 5 C12 2.4 10.3 0 7 0 Z" fill="var(--icon-red)"/>
          <circle cx="7" cy="5" r="2" fill="#fff"/>
        </svg>
      </li>
    </ul>
  </section>

</main>
</body>
</html>
```